College Social website needs a SIMPLE chart design

We need a simple one page website. The website is called "Brev-Onto" a phonetic spelling of the word collage. The site allows users to gain up to date information on the nightlife and social scene of the campus. The site must be able to easily convey several key pieces of information; some type of grid/chart would work well.

This includes:
primary information:
-The name of the bar (about 9 bars on campus)
-The length of the line
-Guy/Girl ratio
-If there is cover (admittance fee) to enter the bar

secondary information:
-how packed/full the bar is
-if there is police raiding the bar
-a way to show more information including drink specials

would prefer a design similar to this page except more colorful/playful/fun: http://m.quillbarrowreg.example/results.php
Updates

Some stylistic tips - the name of the service is called brev onto. a phonetic spelling of collage (http://en.fenwickpedia.example/wiki/Collage). it doesnt need to look like a rainbow, just be exciting, engaging, and vivid.

look at this page for reference: http://www.dravelnook.example/blog/flat-ui-design-showcase/

other than the bar name and drink specials, everything should be presented graphically. All the bar stats are approximations and rough estimates, so you must find a way to present the information as relatives. historical information is not relevant. only the real time stats need to be included. here is a sample:

Bar name: Sample bar
guy/girl ratio: 70/30
line length: short
admittance fee: yes
bar attendance: near full
police raid: no
drink specials:
WINE NIGHT!
$8 BOTTLES OF HALTERMOSS WINE
$8 BOTTLES OF CHAMPAGNE
$2 ZEM GOLD BOTTLES
$2 WELLS

Target Market(s)

target market for the site is 18-21 year olds in college.

Industry/Entity Type

College

Requirements
Must have
• the design MUST be mobile friendly. keep it simple. a flat design would be preferred.
the information must be conveyed in the form of symbols/icons. for instance, a pie chart to show guy/girl ratio.

```html
<!DOCTYPE html>
<html lang="en">
<head>
<meta charset="utf-8">
<title>Brev-Onto — Campus Nightlife</title>
<link rel="stylesheet" href="https://fonts.googleapis.com/css2?family=Roboto+Condensed:wght@400;700&display=swap">
<style>
  :root {
    --ink: #111111;
    --nav-active: #d6245e;
    --rule: #bdbdbd;
    --slate: #4a5868;
    --mustard: #b39516;
    --red: #cc1f1f;
    --orange: #ee6a10;
    --pink: #d6246a;
    --purple: #5b2fd6;
    --band: #161616;
    --row-alt: #f4f4f4;
    --see-more-bg: #d9d9d9;
    --muted: #b8b8b8;
    --white: #ffffff;
  }
  * { box-sizing: border-box; margin: 0; padding: 0; }
  html, body { width: 926px; height: 1200px; overflow: hidden; background: var(--white); }
  body { font-family: "Roboto Condensed", "Arial Narrow", sans-serif; color: var(--ink); }

  .screen {
    position: relative;
    width: 768px;
    height: 995px;
    transform: scale(1.2057);
    transform-origin: 0 0;
    overflow: hidden;
  }

  /* Header */
  .site-header { position: absolute; left: 0; top: 0; width: 768px; height: 80px; border-bottom: 1px solid var(--rule); }
  .site-title { position: absolute; left: 0; right: 0; top: 8px; text-align: center; font-size: 52px; font-weight: 700; letter-spacing: -1px; padding-left: 12px; }
  .social-links { position: absolute; right: 40px; top: 56px; display: flex; gap: 10px; }
  .social-links span { width: 14px; height: 14px; border-radius: 50%; background: var(--ink); display: block; }

  .main-nav { position: absolute; top: 92px; left: 0; width: 768px; height: 20px; font-size: 16px; }
  .main-nav a { position: absolute; color: var(--ink); text-decoration: none; }
  .main-nav a.is-active { color: var(--nav-active); }

  /* Hero */
  .hero { position: absolute; left: 0; top: 0; width: 768px; height: 520px; }
  .hero text { font-family: "Roboto Condensed", "Arial Narrow", sans-serif; }

  .hero-divider { position: absolute; left: 0; top: 513px; width: 768px; height: 7px; border-top: 2px dotted var(--rule); border-bottom: 2px dotted var(--rule); }

  /* Bar table */
  .bar-table { position: absolute; left: 0; top: 527px; width: 768px; }
  .bar-table__head { height: 34px; background: var(--band); color: var(--white); font-size: 20px; font-weight: 700; position: relative; }
  .bar-table__head span { position: absolute; top: 4px; transform: translateX(-50%); }
  .bar-row { position: relative; border-bottom: 2px dashed #9a9a9a; }
  .bar-row:nth-child(odd) { background: var(--row-alt); }
  .bar-row:last-child { border-bottom: none; }
  .bar-row__name { position: absolute; left: 44px; top: 11px; font-size: 19px; font-weight: 700; }
  .bar-row__address { position: absolute; left: 45px; top: 45px; font-size: 13px; color: var(--muted); letter-spacing: .5px; }
  .bar-row__specials, .bar-row__info { position: absolute; top: 10px; font-size: 12px; line-height: 14px; }
  .bar-row__specials { left: 287px; list-style: none; }
  .bar-row__info { left: 504px; width: 240px; }

  .see-more { position: absolute; left: 0; top: 798px; width: 768px; height: 35px; background: var(--see-more-bg); text-align: center; font-size: 19px; font-weight: 700; color: var(--nav-active); line-height: 35px; letter-spacing: .5px; }

  /* Events */
  .video-thumb { position: absolute; left: 44px; top: 852px; width: 218px; height: 110px; background: radial-gradient(circle at 30% 40%, #c03ad8 0%, #3a2fb8 45%, #0f1a6a 100%); }
  .video-thumb__play { position: absolute; left: 84px; top: 34px; }
  .upcoming { position: absolute; left: 499px; top: 855px; width: 240px; }
  .upcoming h2 { font-size: 19px; font-weight: 700; margin-bottom: 8px; letter-spacing: .3px; }
  .upcoming p { font-size: 14px; line-height: 27px; padding-left: 3px; }
</style>
</head>
<body>
<div class="screen">

  <header class="site-header">
    <div class="site-title">BREV-ONTO</div>
    <div class="social-links" aria-label="Social links">
      <span aria-label="social link"></span><span aria-label="social link"></span><span aria-label="social link"></span>
    </div>
  </header>

  <nav class="main-nav">
    <a class="is-active" style="left:97px">HOME</a>
    <a style="left:175px">ABOUT US</a>
    <a style="left:278px">NIGHTLIFE</a>
    <a style="left:381px">EVENTS</a>
    <a style="left:473px">CONTACT US</a>
    <a style="left:596px">WHATS ON?</a>
  </nav>

  <svg class="hero" viewBox="0 0 768 520" width="768" height="520">
    <defs>
      <linearGradient id="tone-warm" x1="0" y1="0" x2="1" y2="1"><stop offset="0" stop-color="#c98a5a"/><stop offset="1" stop-color="#6a3a22"/></linearGradient>
      <linearGradient id="tone-cool" x1="0" y1="0" x2="1" y2="1"><stop offset="0" stop-color="#e8d9b0"/><stop offset="1" stop-color="#5c7ea8"/></linearGradient>
      <linearGradient id="tone-mono" x1="0" y1="0" x2="1" y2="1"><stop offset="0" stop-color="#d0d0d0"/><stop offset="1" stop-color="#2a2a2a"/></linearGradient>
      <linearGradient id="tone-dark" x1="0" y1="0" x2="1" y2="1"><stop offset="0" stop-color="#6a6a6a"/><stop offset="1" stop-color="#0c0c0c"/></linearGradient>
      <linearGradient id="tone-violet" x1="0" y1="0" x2="1" y2="1"><stop offset="0" stop-color="#b9a6e8"/><stop offset="1" stop-color="#3b2a8a"/></linearGradient>
      <linearGradient id="tone-amber" x1="0" y1="0" x2="1" y2="1"><stop offset="0" stop-color="#e0a060"/><stop offset="1" stop-color="#4a2410"/></linearGradient>
      <linearGradient id="badge" x1="0" y1="0" x2="0" y2="1"><stop offset="0" stop-color="#f08a1a"/><stop offset="1" stop-color="#d0300e"/></linearGradient>
      <linearGradient id="ratio-line" x1="0" x2="1"><stop offset="0" stop-color="#5fd0f0"/><stop offset=".35" stop-color="#a6d86a"/><stop offset=".65" stop-color="#f0a060"/><stop offset="1" stop-color="#f07a50"/></linearGradient>
    </defs>

    <!-- Collage tiles -->
    <g class="collage">
      <polygon role="img" aria-label="Photo of a young man at a bar" fill="url(#tone-warm)" points="210,129 260,179 210,229 160,179"/>
      <polygon role="img" aria-label="Photo of a smiling young woman" fill="url(#tone-cool)" points="324,129 374,179 324,229 274,179"/>
      <polygon role="img" aria-label="Black and white photo of a partygoer" fill="url(#tone-mono)" points="443,130 493,180 443,230 393,180"/>
      <polygon role="img" aria-label="Black and white photo of a drink being poured" fill="url(#tone-mono)" points="558,130 608,180 558,230 508,180"/>
      <polygon role="img" aria-label="Photo of friends toasting at a bar" fill="url(#tone-amber)" points="265,190 311,236 265,282 219,236"/>
      <polygon role="img" aria-label="Photo of champagne glasses" fill="url(#tone-dark)" points="501,190 547,236 501,282 455,236"/>
      <polygon role="img" aria-label="Black and white photo of a crowd cheering" fill="url(#tone-dark)" points="265,325 311,371 265,417 219,371"/>
      <polygon role="img" aria-label="Photo of a crowded party" fill="url(#tone-amber)" points="501,325 547,371 501,417 455,371"/>
      <polygon role="img" aria-label="Black and white photo of dancers with raised hands" fill="url(#tone-mono)" points="210,381 260,431 210,481 160,431"/>
      <polygon role="img" aria-label="Photo of a young man on the dance floor" fill="url(#tone-violet)" points="324,381 374,431 324,481 274,431"/>
      <polygon role="img" aria-label="Photo of students at a party" fill="url(#tone-amber)" points="443,381 493,431 443,481 393,431"/>
      <polygon role="img" aria-label="Photo of people laughing together" fill="url(#tone-warm)" points="558,381 608,431 558,481 508,431"/>
      <polygon fill="#ffffff" points="385,195 470,260 385,345 300,260"/>
    </g>

    <!-- Fruit consumption chart -->
    <g class="fruit-chart">
      <text x="385" y="216" text-anchor="middle" font-size="16" font-weight="700" fill="var(--mustard)">FRUIT</text>
      <text x="385" y="240" text-anchor="middle" font-size="16" font-weight="700" fill="var(--mustard)">CONSUMPTION</text>
      <text x="385" y="264" text-anchor="middle" font-size="16" font-weight="700" fill="var(--mustard)">BY DAY</text>
      <text x="302" y="270" font-size="9" text-anchor="end">10</text>
      <text x="302" y="296" font-size="9" text-anchor="end">5</text>
      <text x="302" y="329" font-size="9" text-anchor="end">0</text>
      <line x1="308" y1="326" x2="478" y2="326" stroke="#111" stroke-width="1"/>
      <polygon fill="var(--purple)" points="322,326 322,303 357,310 391,310 425,318 458,296 458,326"/>
      <polyline fill="none" stroke="#c8e6a0" stroke-width="1.5" points="322,298 357,299 391,292 425,290 458,289"/>
      <polyline fill="none" stroke="#e05ab0" stroke-width="1.2" points="322,309 357,318 391,306 425,317 460,262"/>
      <g font-size="9" text-anchor="middle">
        <text x="325" y="337">MON</text><text x="357" y="337">TUE</text><text x="391" y="337">WED</text><text x="425" y="337">THU</text><text x="455" y="337">FRI</text>
      </g>
      <text x="387" y="364" text-anchor="middle" font-size="12" fill="var(--red)">SATURDAY &amp; SUNDAY</text>
      <text x="381" y="384" text-anchor="middle" font-size="12" fill="var(--red)">SPECIALS ....</text>
    </g>

    <!-- Guy / girl ratio -->
    <g class="ratio">
      <text x="52" y="215" font-size="13" font-weight="700" fill="var(--slate)">GUY/GIRL RATIO</text>
      <rect x="135" y="239" width="48" height="39" fill="url(#badge)"/>
      <text x="159" y="256" text-anchor="middle" font-size="13" font-weight="700">80%</text>
      <text x="161" y="273" text-anchor="middle" font-size="13" font-weight="700">FULL</text>
      <line x1="45" y1="278" x2="226" y2="278" stroke="url(#ratio-line)" stroke-width="3"/>
      <text x="77" y="306" font-size="14" font-weight="700">70%</text>
      <text x="170" y="306" font-size="14" font-weight="700">30%</text>
      <line x1="60" y1="323" x2="206" y2="323" stroke="var(--red)" stroke-width="3"/>
      <line x1="150" y1="323" x2="206" y2="323" stroke="var(--orange)" stroke-width="3"/>
      <circle cx="58" cy="323" r="16" fill="var(--red)"/>
      <circle cx="208" cy="323" r="16" fill="var(--orange)"/>
      <g fill="#ffffff">
        <circle cx="58" cy="314" r="3"/><rect x="55" y="318" width="6" height="14" rx="2"/>
        <circle cx="208" cy="314" r="3"/><polygon points="208,317 214,328 202,328"/><rect x="206" y="327" width="4" height="6"/>
      </g>
    </g>

    <!-- Drink specials -->
    <g class="specials" font-size="11" fill="#ffffff">
      <text x="733" y="215" text-anchor="end" font-size="13" font-weight="700" fill="var(--slate)">DRINK SPECIALS</text>
      <rect x="610" y="229" width="123" height="17" fill="var(--red)"/><text x="671" y="241" text-anchor="middle">BAR IS ALMOST FULL</text>
      <rect x="595" y="251" width="138" height="17" fill="var(--orange)"/><text x="664" y="263" text-anchor="middle">ADMITTANCE FEE NEEDED</text>
      <rect x="535" y="275" width="198" height="17" fill="var(--pink)"/><text x="638" y="287" text-anchor="middle">$8 BOTTLES OF HALTERMOSS WINE</text>
      <rect x="550" y="299" width="183" height="17" fill="var(--red)"/><text x="628" y="311" text-anchor="middle">$8 BOTTLES OF CHAMPAGNE</text>
      <rect x="565" y="323" width="168" height="17" fill="var(--orange)"/><text x="645" y="335" text-anchor="middle">$2 ZEM GOLD BOTTLES</text>
      <rect x="608" y="347" width="125" height="17" fill="var(--pink)"/><text x="643" y="359" text-anchor="middle">$2 WELLS</text>
      <rect x="602" y="372" width="131" height="17" fill="var(--red)"/><text x="665" y="384" text-anchor="middle">NO POLICE RAID</text>
      <rect x="635" y="397" width="98" height="17" fill="var(--orange)"/><text x="686" y="409" text-anchor="middle">LINE SHORT</text>
    </g>

    <!-- Slider dots -->
    <g class="slider-dots" fill="#8a8a8a">
      <circle cx="349" cy="497" r="4"/><circle cx="370" cy="497" r="4" fill="var(--nav-active)"/><circle cx="392" cy="497" r="4"/><circle cx="414" cy="497" r="4"/>
    </g>
  </svg>

  <div class="hero-divider"></div>

  <section class="bar-table">
    <div class="bar-table__head">
      <span style="left:109px">BARS</span>
      <span style="left:385px">DRINK SPECIALS</span>
      <span style="left:620px">INFORMATION</span>
    </div>

    <div class="bar-rows">
      <article class="bar-row" style="height:73px; background:#fff">
        <h3 class="bar-row__name">THE NAME OF THE BAR</h3>
        <p class="bar-row__address">ADDRESS</p>
        <ul class="bar-row__specials"><li>$8 BOTTLES OF HALTERMOSS WINE</li><li>$8 BOTTLES OF CHAMPAGNE</li><li>$2 ZEM GOLD BOTTLES</li><li>$2 WELLS</li></ul>
        <p class="bar-row__info">“Lorem Ipsum is simply dummy text of the printing and typesetting industry. Lorem Ipsum has been the industry's standard dummy text ever since the 1500s, when an unknown” printer</p>
      </article>
      <article class="bar-row" style="height:83px">
        <h3 class="bar-row__name">THE NAME OF THE BAR</h3>
        <p class="bar-row__address">ADDRESS</p>
        <ul class="bar-row__specials"><li>$8 BOTTLES OF HALTERMOSS WINE</li><li>$8 BOTTLES OF CHAMPAGNE</li><li>$2 ZEM GOLD BOTTLES</li><li>$2 WELLS</li></ul>
        <p class="bar-row__info">“Lorem Ipsum is simply dummy text of the printing and typesetting industry. Lorem Ipsum has been the industry's standard dummy text ever since the 1500s, when an unknown” printer</p>
      </article>
      <article class="bar-row" style="height:81px; background:#fff">
        <h3 class="bar-row__name">THE NAME OF THE BAR</h3>
        <p class="bar-row__address">ADDRESS</p>
        <ul class="bar-row__specials"><li>$8 BOTTLES OF HALTERMOSS WINE</li><li>$8 BOTTLES OF CHAMPAGNE</li><li>$2 ZEM GOLD BOTTLES</li><li>$2 WELLS</li></ul>
        <p class="bar-row__info">“Lorem Ipsum is simply dummy text of the printing and typesetting industry. Lorem Ipsum has been the industry's standard dummy text ever since the 1500s, when an unknown” printer</p>
      </article>
    </div>
  </section>

  <div class="see-more">SEE MORE...</div>

  <div class="video-thumb" role="img" aria-label="Video still of a crowded dance floor under purple lights">
    <svg class="video-thumb__play" width="54" height="54" viewBox="0 0 54 54">
      <circle cx="27" cy="27" r="25" fill="#dfe6ee" stroke="#8a9ab0" stroke-width="2"/>
      <circle cx="27" cy="27" r="19" fill="#2a5db0"/>
      <polygon points="21,16 37,27 21,38" fill="#ffffff"/>
    </svg>
  </div>

  <section class="upcoming">
    <h2>UPCOMING EVENTS</h2>
    <p>“Lorem Ipsum is simply dummy text of the printing and typesetting industry. Lorem Ipsum has been the industry's</p>
  </section>

</div>
</body>
</html>
```